In need of a production and engineering website design

In need of a website design for my Rap/Hip-Hop Production & Engineering Business. Name can be changed, to fit the idea of the best design but must closely resemble the idea of the first name (ex. Loops by Tavel, Prod. By Tavel, etc.).

The text and design will be in any format but must be eye catching and appeal to a young audience (i.e. attractive design), to include functions preview beats player, clickable catalog for purchasing (using Cashlyn) and a "request for booking" tab for artists, to be used in email format as supposed to a contact me form. Please use generalization tabs such as "Catalog" instead of "buy" or "sell" as these terms do not fit the business model. You may also use "Purchase Beats" instead of Catalog; whatever fits your design will work.

Social Media Links (Chirpex, ViewReel, Pagemoot, AudioDrift, Holvane+, Glimra, Tradewell (professional resource), etc.) and FAQ page as supposed to a who am I page (bio);

Note: FAQ Page wont be necessary needed for the design portion but would be nice to let the designer know my intentions.

Please use the supplied logo and/or images for your project.

The final design should communicate production/engineer knowledge and potential for music industry growth. (the logo will communicate the same)

Project Deadline Extended Reason: To Provide more time to the competition; To Provide stock pictures and logo designs to make competition more challenging. Added Sunday, June 26, 2016

This site has not been finished by the current designer. He has lacked the necessary communication, implementation of above directives and has neglected to professionally develop and finish the site. Though he has been hired to code the site. His negligence reflects great discredit upon his work and will receive a bad review with this site as reference. He may try to fix his reviews or change his name...either way, I will be there to reference this site as his handiwork. Thanks guy but you did not finish coding the site...which means your dedication to code and development has not finished and I will be looking to recoup the one-on-one if you decide to keep avoiding to finish the previously mentioned and direct messaged objectives which took a whole team to decide on. Thanks.

Target Market(s)

A&R Management Firms (Music), Musicians, Music Artists, Business Entrepreneurs, Etc.

Industry/Entity Type

Music Download

Number of Pages Required

5+ page

Requirements
Must have
• Preview, Select, and Pay options (beats catalog), Bio, Mix/Mastering Services, Contact, Live Talvo Chat, Social Media Networking, FAQ / TOS, the option to code all the work (will add the additional fee to the winning artist), the ability to exchange user's email in return for a free HQ lease of their choice every month starting the 30th day of each month as long as they maintain their subscription status.
Nice to have
• General Merchandise page and a user / admin login and register system buttons and a dedicated blog page (if hired to code, this will be a requirement).
• Those will receive a review if designed: Cell Phone condensed version (w/ buttons to lease and buy on the left side of each song within the playlist)
Should not have
• Copyrighted material, anything not of this generation but must have a keen resemblance of the 2000's to 2010's hip hop trap or rap community.

```html
<!DOCTYPE html>
<html lang="en">
<head>
<meta charset="utf-8">
<title>Loops by Tavel — Rap/Hip-Hop Production &amp; Engineering</title>
<link rel="stylesheet" href="https://fonts.googleapis.com/css2?family=Lora:wght@400&family=Open+Sans:wght@400;600&family=Raleway:wght@500&display=swap">
<style>
:root{
  --black:#050505;
  --orange:#e8830c;
  --orange-deep:#e27c00;
  --white:#ffffff;
  --ink:#222222;
  --grey:#8a8a8a;
  --line:#dddddd;
  --footer:#2b2b2b;
  --chat:#1aa3e0;
}
*{margin:0;padding:0;box-sizing:border-box}
html,body{width:1200px;height:2479px;overflow:hidden}
body{position:relative;background:var(--white);font-family:"Open Sans",sans-serif;color:var(--ink)}
h1,h2,h3{font-weight:400}
.abs{position:absolute}

/* header */
.site-header{left:0;top:0;width:1200px;height:97px;background:var(--black)}
.brand{left:129px;top:28px;font-family:"Lora",serif;font-size:29px;color:var(--white)}
.brand span{color:var(--orange)}
.main-nav{right:129px;top:42px;display:flex;gap:34px;font-family:"Raleway",sans-serif;font-weight:500;font-size:13.5px;color:var(--white)}
.main-nav .active{color:var(--orange)}

/* hero */
.hero{left:0;top:97px;width:1200px;height:476px}
.hero-title{left:0;top:252px;width:1200px;text-align:center;font-family:"Lora",serif;font-weight:400;color:var(--white);text-shadow:0 2px 8px rgba(0,0,0,.5)}
.hero-title .l1{display:block;font-size:48px;line-height:58px}
.hero-title .l2{display:block;font-size:35px;line-height:44px}
.hero-dots{left:563px;top:536px;display:flex;gap:5px}
.hero-dots i{width:14px;height:14px;border-radius:50%;background:var(--white);border:2px solid var(--white)}
.hero-dots i:first-child{background:transparent}

/* about */
.about-photo{left:0;top:573px;width:598px;height:407px}
.about-panel{left:598px;top:573px;width:602px;height:407px;background:var(--orange-deep);color:var(--white)}
.about-panel h2{position:absolute;left:51px;top:68px;font-family:"Lora",serif;font-weight:400;font-size:35px}
.about-panel .lead{position:absolute;left:51px;top:127px;width:380px;font-size:13px;line-height:21px}
.about-panel .body{position:absolute;left:51px;top:183px;width:380px;font-size:11.5px;line-height:20px}
.btn-outline{position:absolute;left:51px;top:282px;width:125px;height:38px;border:2px solid var(--white);color:var(--white);font-size:13.5px;line-height:34px;text-align:center}

/* beats player */
.player-bg{left:330px;top:1000px;width:560px;height:500px}
.section-title{font-family:"Lora",serif;font-weight:400;font-size:27px;color:var(--ink)}
.player-title{left:129px;top:1030px}
.track{width:460px;height:100px}
.track-cover{position:absolute;left:0;top:0;width:100px;height:100px;border-radius:50%}
.play{position:absolute;left:35px;top:35px;width:30px;height:30px}
.track-name{position:absolute;left:118px;top:2px;font-size:15px;color:var(--orange)}
.track-desc{position:absolute;left:118px;top:26px;width:320px;font-size:11.5px;line-height:20px;color:var(--grey)}
.track-link{position:absolute;left:118px;top:71px;font-size:12px;color:var(--ink)}

/* booking */
.booking-band{left:0;top:1510px;width:1200px;height:430px}
.booking-title{left:0;top:1588px;width:1200px;text-align:center;font-family:"Lora",serif;font-weight:400;font-size:30px;color:var(--white)}
.booking-sub{left:0;top:1632px;width:1200px;text-align:center;font-size:15px;color:rgba(255,255,255,.8)}
.field{background:var(--white);border-radius:2px;font-size:12.5px;color:#9a9a9a;padding:9px 14px}
.btn-submit{left:542px;top:1827px;width:118px;height:36px;background:var(--orange);color:var(--white);font-size:13px;font-weight:600;text-align:center;line-height:36px}

/* catalog */
.catalog-title{left:0;top:1938px;width:1200px;text-align:center;font-family:"Lora",serif;font-weight:400;font-size:24px;color:var(--orange)}
.card{top:1990px;width:228px;height:268px;border:1px solid var(--line);background:var(--white)}
.card-img{position:absolute;left:10px;top:11px;width:208px;height:137px}
.card h3{position:absolute;left:16px;top:158px;font-weight:400;font-size:14.5px;color:var(--ink)}
.card p{position:absolute;left:16px;top:181px;width:200px;font-size:11px;line-height:19px;color:var(--grey)}
.btn-small{position:absolute;left:16px;top:227px;width:88px;height:28px;border:1.5px solid var(--orange);color:var(--orange);font-size:11px;text-align:center;line-height:25px}

/* footer */
.site-footer{left:0;top:2322px;width:1200px;height:157px;background:var(--footer);border-top:4px solid var(--orange)}
.footer-nav{position:absolute;left:129px;top:36px;display:flex;gap:26px;font-family:"Raleway",sans-serif;font-weight:500;font-size:12px;color:var(--white)}
.copyright{position:absolute;left:129px;top:64px;font-size:11px;color:#a8a8a8}
.social{position:absolute;right:129px;top:34px;display:flex;gap:9px;font-size:11.5px;font-weight:600;color:var(--white)}
.chat-btn{position:absolute;left:708px;top:78px;width:137px;height:34px;background:var(--chat);color:var(--white);font-size:12px;display:flex;align-items:center;gap:8px;padding-left:8px}
.chat-btn i{width:16px;height:16px;border-radius:50%;background:var(--white)}
.pay{position:absolute;left:872px;top:82px;display:flex;gap:6px}
.pay span{width:36px;height:24px;background:var(--white);border-radius:2px;font-size:8.5px;font-weight:600;color:#333;text-align:center;line-height:24px}
</style>
</head>
<body>

<header class="site-header abs">
  <div class="brand abs">Loops by <span>Tavel</span></div>
  <nav class="main-nav abs">
    <a class="active">HOME</a><a>PREVIEW</a><a>SELL BEATS</a><a>SELL MIX/MASTERING SERVICES</a><a>CONTACT</a>
  </nav>
</header>

<svg class="hero abs" role="img" aria-label="Rapper performing into a microphone under coloured stage lights" viewBox="0 0 1200 476" preserveAspectRatio="none">
  <defs>
    <linearGradient id="heroGrad" x1="0" y1="0" x2="1" y2="1">
      <stop offset="0" stop-color="#3a2b55"/>
      <stop offset=".35" stop-color="#8a3f2a"/>
      <stop offset=".6" stop-color="#5a2a4a"/>
      <stop offset="1" stop-color="#1a1a28"/>
    </linearGradient>
    <radialGradient id="heroGlow" cx=".45" cy=".25" r=".55">
      <stop offset="0" stop-color="#f0a040" stop-opacity=".55"/>
      <stop offset="1" stop-color="#f0a040" stop-opacity="0"/>
    </radialGradient>
  </defs>
  <rect width="1200" height="476" fill="url(#heroGrad)"/>
  <rect width="1200" height="476" fill="url(#heroGlow)"/>
</svg>
<h1 class="hero-title abs"><span class="l1">Rap/Hip-Hop Production &amp;</span><span class="l2">Engineering Business</span></h1>
<div class="hero-dots abs"><i></i><i></i><i></i><i></i></div>

<svg class="about-photo abs" role="img" aria-label="Artist in a cap singing on a purple-lit stage" viewBox="0 0 598 407" preserveAspectRatio="none">
  <defs>
    <linearGradient id="aboutGrad" x1="0" y1="0" x2="1" y2="1">
      <stop offset="0" stop-color="#3a1a8a"/>
      <stop offset=".55" stop-color="#6a1a9a"/>
      <stop offset="1" stop-color="#c040d0"/>
    </linearGradient>
  </defs>
  <rect width="598" height="407" fill="url(#aboutGrad)"/>
</svg>
<section class="about-panel abs">
  <h2>About Me</h2>
  <p class="lead">Suspendisse quam leo molestie sed luctus quis feugiat in pede Fusce tellus Sed metus augue convallis</p>
  <p class="body">Apulvinar eu ante Integer orci tellus tristique vitae consequat nec porta vel lectus Nulla sit amet diam Duis non nunc Nulla rhoncus dictum metus Curabitur tristique mi condimentum orcus Ut ac mi quis lacus mollis aliquam Curabitur iaculis tempus eros</p>
  <a class="btn-outline">Learn More</a>
</section>

<svg class="player-bg abs" role="img" aria-label="Faint backdrop of a breakdancer mid-jump" viewBox="0 0 560 500" preserveAspectRatio="none">
  <defs>
    <radialGradient id="dancerGrad" cx=".5" cy=".45" r=".5">
      <stop offset="0" stop-color="#d8d8d8" stop-opacity=".55"/>
      <stop offset="1" stop-color="#ffffff" stop-opacity="0"/>
    </radialGradient>
  </defs>
  <rect width="560" height="500" fill="url(#dancerGrad)"/>
</svg>
<h2 class="section-title player-title abs">Beats Player</h2>

<div class="track abs" style="left:135px;top:1094px">
  <div class="track-cover" role="img" aria-label="Cover art: DJ at the turntables" style="background:radial-gradient(circle,#8a7a50,#2a2418)"></div>
  <svg class="play" viewBox="0 0 30 30"><circle cx="15" cy="15" r="15" fill="#fff"/><path d="M12 9l9 6-9 6z" fill="#222"/></svg>
  <div class="track-name">Morbi diam mauris viverra</div>
  <p class="track-desc">gravida eu mattis in ante Morbi eget arcu Morbi porta libero id ullamcorper nonummy nibh ligula</p>
  <div class="track-link">Listen Now</div>
</div>
<div class="track abs" style="left:607px;top:1094px">
  <div class="track-cover" role="img" aria-label="Cover art: performer on a warm-lit stage" style="background:radial-gradient(circle,#b0705a,#3a1e2a)"></div>
  <svg class="play" viewBox="0 0 30 30"><circle cx="15" cy="15" r="15" fill="#fff"/><path d="M12 9l9 6-9 6z" fill="#222"/></svg>
  <div class="track-name">Morbi diam mauris viverra</div>
  <p class="track-desc">gravida eu mattis in ante Morbi eget arcu Morbi porta libero id ullamcorper nonummy nibh ligula</p>
  <div class="track-link">Listen Now</div>
</div>
<div class="track abs" style="left:135px;top:1220px">
  <div class="track-cover" role="img" aria-label="Cover art: vinyl record deck" style="background:radial-gradient(circle,#9a7a5a,#1e1a18)"></div>
  <svg class="play" viewBox="0 0 30 30"><circle cx="15" cy="15" r="15" fill="#fff"/><path d="M12 9l9 6-9 6z" fill="#222"/></svg>
  <div class="track-name">Morbi diam mauris viverra</div>
  <p class="track-desc">gravida eu mattis in ante Morbi eget arcu Morbi porta libero id ullamcorper nonummy nibh ligula</p>
  <div class="track-link">Listen Now</div>
</div>
<div class="track abs" style="left:607px;top:1220px">
  <div class="track-cover" role="img" aria-label="Cover art: hands on a mixing controller" style="background:radial-gradient(circle,#a06a40,#1e1410)"></div>
  <svg class="play" viewBox="0 0 30 30"><circle cx="15" cy="15" r="15" fill="#fff"/><path d="M12 9l9 6-9 6z" fill="#222"/></svg>
  <div class="track-name">Morbi diam mauris viverra</div>
  <p class="track-desc">gravida eu mattis in ante Morbi eget arcu Morbi porta libero id ullamcorper nonummy nibh ligula</p>
  <div class="track-link">Listen Now</div>
</div>
<div class="track abs" style="left:135px;top:1342px">
  <div class="track-cover" role="img" aria-label="Cover art: DJ under teal club lights" style="background:radial-gradient(circle,#3a6a6a,#0e1a1e)"></div>
  <svg class="play" viewBox="0 0 30 30"><circle cx="15" cy="15" r="15" fill="#fff"/><path d="M12 9l9 6-9 6z" fill="#222"/></svg>
  <div class="track-name">Morbi diam mauris viverra</div>
  <p class="track-desc">gravida eu mattis in ante Morbi eget arcu Morbi porta libero id ullamcorper nonummy nibh ligula</p>
  <div class="track-link">Listen Now</div>
</div>
<div class="track abs" style="left:607px;top:1342px">
  <div class="track-cover" role="img" aria-label="Cover art: vintage boombox" style="background:radial-gradient(circle,#7a7a7a,#141414)"></div>
  <svg class="play" viewBox="0 0 30 30"><circle cx="15" cy="15" r="15" fill="#fff"/><path d="M12 9l9 6-9 6z" fill="#222"/></svg>
  <div class="track-name">Morbi diam mauris viverra</div>
  <p class="track-desc">gravida eu mattis in ante Morbi eget arcu Morbi porta libero id ullamcorper nonummy nibh ligula</p>
  <div class="track-link">Listen Now</div>
</div>

<svg class="booking-band abs" role="img" aria-label="Glowing stage backdrop with drifting sparks and red-orange light" viewBox="0 0 1200 430" preserveAspectRatio="none">
  <defs>
    <radialGradient id="bookGrad" cx=".55" cy=".55" r=".6">
      <stop offset="0" stop-color="#e0603a"/>
      <stop offset=".45" stop-color="#8a1e4a"/>
      <stop offset="1" stop-color="#150a1e"/>
    </radialGradient>
  </defs>
  <path fill="url(#bookGrad)" d="M0 25 C30 15 45 35 70 20 C95 5 115 45 140 30 C165 15 175 60 200 40 C230 20 245 5 270 25 C295 45 310 65 335 40 C360 15 380 10 405 30 C430 50 450 35 475 20 C500 5 520 40 545 35 C570 30 590 60 615 40 C640 20 660 10 690 30 C720 50 740 65 765 45 C790 25 805 5 830 20 C855 35 870 60 895 40 C920 20 940 15 965 30 C990 45 1010 55 1035 35 C1060 15 1080 10 1105 30 C1130 50 1150 40 1175 25 C1190 15 1200 20 1200 20 L1200 380 C1175 400 1160 360 1135 385 C1110 410 1090 370 1065 390 C1040 410 1020 430 995 400 C970 370 950 395 925 410 C900 425 880 375 855 390 C830 405 810 425 785 400 C760 375 740 390 715 410 C690 430 670 385 645 395 C620 405 600 425 575 400 C550 375 530 395 505 410 C480 425 460 380 435 390 C410 400 390 420 365 400 C340 380 320 395 295 410 C270 425 250 385 225 395 C200 405 180 420 155 400 C130 380 110 395 85 410 C60 425 40 385 20 395 L0 400 Z"/>
</svg>
<h2 class="booking-title abs">Request for Booking</h2>
<p class="booking-sub abs">Ut ac mi quis lacus mollis aliquam Curabitur iaculis tempus eros Curabitur vel mi sit</p>
<div class="field abs" style="left:268px;top:1683px;width:220px;height:35px">Name</div>
<div class="field abs" style="left:497px;top:1683px;width:220px;height:35px">Email address</div>
<div class="field abs" style="left:726px;top:1683px;width:220px;height:35px">Phone</div>
<div class="field abs" style="left:268px;top:1728px;width:678px;height:86px">Message</div>
<a class="btn-submit abs">SUBMIT</a>

<h2 class="catalog-title abs">BUY CATALOG</h2>

<article class="card abs" style="left:127px">
  <div class="card-img" role="img" aria-label="Mixing desk under purple light" style="background:linear-gradient(135deg,#5a3a9a,#1e1030)"></div>
  <h3>Aculis facilisis massa</h3>
  <p>Etiam eu urna Sed porta Suspend-isse quam leo molestie</p>
  <a class="btn-small">BUY NOW</a>
</article>
<article class="card abs" style="left:367px">
  <div class="card-img" role="img" aria-label="Black and white boombox" style="background:linear-gradient(135deg,#9a9a9a,#1a1a1a)"></div>
  <h3>Aculis facilisis massa</h3>
  <p>Etiam eu urna Sed porta Suspend-isse quam leo molestie</p>
  <a class="btn-small">BUY NOW</a>
</article>
<article class="card abs" style="left:607px">
  <div class="card-img" role="img" aria-label="DJ at decks with warm spotlights" style="background:linear-gradient(135deg,#1e2a5a,#b04a3a)"></div>
  <h3>Aculis facilisis massa</h3>
  <p>Etiam eu urna Sed porta Suspend-isse quam leo molestie</p>
  <a class="btn-small">BUY NOW</a>
</article>
<article class="card abs" style="left:847px">
  <div class="card-img" role="img" aria-label="Hooded artist against a cloudy sky" style="background:linear-gradient(135deg,#7a8a9a,#1a1e24)"></div>
  <h3>Aculis facilisis massa</h3>
  <p>Etiam eu urna Sed porta Suspend-isse quam leo molestie</p>
  <a class="btn-small">BUY NOW</a>
</article>

<footer class="site-footer abs">
  <nav class="footer-nav">
    <a>HOME</a><a>PREVIEW</a><a>SELL BEATS</a><a>SELL MIX/MASTERING SERVICES</a><a>CONTACT</a>
  </nav>
  <p class="copyright">© 2016 Company Name &nbsp;All right reserved &nbsp;Term of Use</p>
  <div class="social">
    <a>Pagemoot</a><a>Chirpex</a><a>Tradewell</a><a>Holvane+</a><a>ViewReel</a><a>AudioDrift</a><a>Glimra</a>
  </div>
  <a class="chat-btn"><i></i>Live Talvo Chat</a>
  <div class="pay">
    <span>Pelta</span><span>Zorama</span><span>Tessly</span><span>Quillon</span><span>Cashlyn</span>
  </div>
</footer>

</body>
</html>
```